Kelpa Stride - Graphic Label

Company Name: Verdant Pillar
Product: Organic Energy Drink
Name of Drink : Kelpa Stride
8.45oz - Bottle
http://www.tradobin-example.com/item-view/Metal-drink-bottle-sample_4928061735.html?r=q
Attached will be examples of labels for other drinks associated with this company along with company logo. I'm open to all interpretations of design. Please submit creative ideas and we can adjust design as we go.
Design must have some integration of the geometry as seen in labels attached.
Keep it classy
If you have a vision for the design, just create it and we can adjust from there.
I want the bottle to have long lasting but creative/interesting design..
Reason: Design sought has not been submited, the deadline has been extended.
Please continue submissions.
- Thanks
Target Market(s)
All Ages .. those interested in Organics, health drinks, energy drinks
Industry/Entity Type
It Company

```html
<!DOCTYPE html>
<html lang="en">
<head>
<meta charset="utf-8">
<title>Kelpa Stride – Organic Energy Drink Label</title>
<link rel="stylesheet" href="https://fonts.googleapis.com/css2?family=Limelight&family=Indie+Flower&family=Josefin+Sans:wght@600&display=swap">
<style>
  :root {
    --page: #f4f5f4;
    --label-black: #050605;
    --label-green: #1f4a2a;
    --label-green-deep: #163a20;
    --leaf: #3f8a2f;
    --leaf-dark: #1e5a1c;
    --fruit: #f1d22a;
    --pennant: #9aa83a;
    --silver-top: #ffffff;
    --silver-bottom: #b9bdbf;
    --script-green: #7ec24a;
    --small-white: #e8ece8;
  }
  html, body {
    margin: 0;
    width: 1200px;
    height: 983px;
    overflow: hidden;
    background: var(--page);
  }
  .label {
    position: absolute;
    left: 50px;
    top: 38px;
    width: 1100px;
    height: 907px;
    overflow: hidden;
    background: var(--label-green);
  }
  .label-field { position: absolute; inset: 0; }
  .art {
    position: absolute;
    border-radius: 46% 54% 50% 50%;
  }
  .art-fruit {
    left: 205px; top: 12px; width: 315px; height: 412px;
    background: radial-gradient(ellipse at 60% 45%, var(--fruit) 0 34%, var(--leaf) 36%, var(--leaf-dark) 70%, transparent 72%);
  }
  .art-leaves-left {
    left: -40px; top: -20px; width: 200px; height: 600px;
    background: radial-gradient(ellipse at 40% 50%, var(--leaf) 0 40%, var(--leaf-dark) 62%, transparent 70%);
  }
  .art-leaves-right {
    left: 930px; top: 327px; width: 210px; height: 600px;
    background: radial-gradient(ellipse at 60% 50%, var(--leaf) 0 38%, var(--leaf-dark) 60%, transparent 70%);
  }
  .art-leaves-top {
    left: 785px; top: -40px; width: 340px; height: 130px;
    background: radial-gradient(ellipse at 50% 45%, var(--leaf) 0 35%, var(--leaf-dark) 58%, transparent 70%);
  }
  .art-leaves-bottom {
    left: 660px; top: 830px; width: 190px; height: 110px;
    background: radial-gradient(ellipse at 50% 55%, var(--leaf) 0 35%, var(--leaf-dark) 58%, transparent 70%);
  }
  .cert-badge {
    position: absolute;
    left: 51px; top: 8px;
    width: 58px; height: 58px;
    border-radius: 50%;
    background: #ffffff;
    box-shadow: inset 0 0 0 5px #2b6c34;
  }
  .brand-pennant {
    position: absolute;
    left: 290px; top: 0;
    width: 86px; height: 100px;
    background: var(--pennant);
    clip-path: polygon(0 0, 100% 0, 100% 78%, 50% 100%, 0 78%);
    display: flex;
    align-items: center;
    justify-content: center;
    text-align: center;
  }
  .brand-name {
    font-family: "Josefin Sans", sans-serif;
    font-weight: 600;
    font-size: 11px;
    line-height: 1.1;
    color: #f4f6e4;
    margin-top: -10px;
  }
  .product-name {
    position: absolute;
    left: 210px; top: 410px;
    width: 500px;
    margin: 0;
    text-align: center;
    font-family: "Limelight", sans-serif;
    font-weight: 400;
    font-size: 128px;
    line-height: 0.92;
    letter-spacing: 2px;
    background: linear-gradient(var(--silver-top), var(--silver-bottom));
    -webkit-background-clip: text;
    background-clip: text;
    color: transparent;
  }
  .tagline {
    position: absolute;
    left: 210px; top: 752px;
    width: 500px;
    text-align: center;
    font-family: "Indie Flower", cursive;
    font-size: 42px;
    color: var(--script-green);
  }
  .volume {
    position: absolute;
    left: 625px; top: 850px;
    font-family: "Josefin Sans", sans-serif;
    font-weight: 600;
    font-size: 20px;
    letter-spacing: 1px;
    color: var(--small-white);
  }
</style>
</head>
<body>
  <main class="label">
    <svg class="label-field" width="1100" height="907" viewBox="0 0 1100 907" aria-hidden="true">
      <rect width="1100" height="907" fill="var(--label-green)"/>
      <path d="M140 907 L140 330 C140 150 300 60 520 0 L820 0 C960 230 1010 560 990 907 Z" fill="var(--label-black)"/>
      <path d="M820 0 C960 230 1010 560 990 907 L1010 907 C1030 560 980 230 845 0 Z" fill="var(--label-green-deep)"/>
    </svg>

    <div class="art art-leaves-left" role="img" aria-label="Green leaves along the left edge"></div>
    <div class="art art-leaves-top" role="img" aria-label="Green leaves at the top right corner"></div>
    <div class="art art-leaves-right" role="img" aria-label="Green leaves along the right edge"></div>
    <div class="art art-leaves-bottom" role="img" aria-label="Green leaves at the bottom edge"></div>
    <div class="art art-fruit" role="img" aria-label="Yellow fruit hanging among green leaves"></div>

    <div class="cert-badge" role="img" aria-label="Organic certification badge"></div>

    <div class="brand-pennant">
      <span class="brand-name">Verdant<br>Pillar</span>
    </div>

    <h1 class="product-name">KELPA<br>STRIDE</h1>
    <p class="tagline" style="margin:0">Organic Energy Drink</p>
    <p class="volume" style="margin:0">8.45 OZ.</p>
  </main>
</body>
</html>
```